Quimby's Yard & Garden Center Business Card Update

I need an updated Business card design for my Lawn and Garden Center. We do Landscaping installs, Lawn Mowing, Snow Removal and also have a Garden Center Retail Division. I uploaded a few of our previous business cards to give an idea of what we are starting with. The main goal of this update is to simplify and modernize the business card, not all of the services that are on the previous cards has to be on the new one but I would still like to highlight our main services. There is also a sample of our logo that Can be used in the design.

Industry/Entity Type

Landscaping

Contact Information for Business Card

Morris Quimby
Morris@Quimbysyardandgarden.example
Business (555) 201-7784
Cell (555) 318-6092

Colors

Designer to choose colors to be used in the design.

Requirements
Must have
• Services Provided :
• Landscaping
• Lawn Maintenance
• Snow Removal
• Garden Center

```html
<!DOCTYPE html>
<html lang="en">
<head>
<meta charset="utf-8">
<title>Quimby's Yard &amp; Garden Center – Business Card</title>
<link rel="stylesheet" href="https://fonts.googleapis.com/css2?family=Open+Sans:wght@400;600;700&family=Courgette&display=swap">
<style>
  :root {
    --green: #2e5a27;
    --green-dark: #264d21;
    --orange: #e9a33b;
    --white: #ffffff;
    --paper: #f3f3f3;
    --ink: #1e3d1a;
    --stage: #e6e6e4;
  }
  * { box-sizing: border-box; margin: 0; padding: 0; }
  html, body { width: 1200px; height: 1021px; overflow: hidden; background: var(--stage); }
  body { font-family: "Open Sans", Arial, sans-serif; }
  .stage {
    width: 1200px; height: 1021px;
    display: flex; flex-direction: column; align-items: center; justify-content: center; gap: 40px;
  }
  .card {
    position: relative; width: 800px; height: 457px; overflow: hidden;
    box-shadow: 0 6px 18px rgba(0,0,0,.18);
  }
  /* Back side */
  .card--back { background: var(--green); color: var(--white); }
  .tagline {
    position: absolute; left: 0; right: 0; top: 130px; text-align: center;
    font-family: "Courgette", cursive; font-size: 46px; color: var(--orange);
  }
  .services {
    position: absolute; left: 0; right: 0; top: 215px; list-style: none; text-align: center;
    font-weight: 600; font-size: 22px; letter-spacing: .5px; line-height: 1.4; text-transform: uppercase;
  }
  /* Front side */
  .card--front { background: linear-gradient(180deg, var(--white), var(--paper)); }
  .card__band { position: absolute; inset: 0; }
  .person { position: absolute; left: 44px; top: 38px; }
  .person__name { font-weight: 700; font-size: 25px; color: var(--green); text-transform: uppercase; }
  .person__role { font-size: 15px; color: #333; text-transform: uppercase; }
  .brand {
    position: absolute; left: 0; right: 0; top: 150px; text-align: center;
    font-weight: 700; font-size: 32px; color: var(--ink);
  }
  .address {
    position: absolute; left: 44px; bottom: 110px; color: var(--white); font-size: 18px; line-height: 1.35;
  }
  .contact {
    position: absolute; right: 40px; bottom: 34px; list-style: none; color: var(--white);
    font-size: 18px; line-height: 1.45; text-align: right;
  }
  .contact li { display: flex; align-items: center; justify-content: flex-end; gap: 10px; }
  .contact svg { width: 18px; height: 18px; fill: none; stroke: var(--white); stroke-width: 1.8; }
</style>
</head>
<body>
<main class="stage">
  <section class="card card--back" aria-label="Card back">
    <p class="tagline">Where Color Lives...</p>
    <ul class="services">
      <li>Landscaping</li>
      <li>Lawn Maintenance</li>
      <li>Snow Removal</li>
      <li>Garden Center</li>
    </ul>
  </section>

  <section class="card card--front" aria-label="Card front">
    <svg class="card__band" viewBox="0 0 800 457" preserveAspectRatio="none" aria-hidden="true">
      <path d="M0,200 C260,300 560,320 800,280 L800,457 L0,457 Z" fill="var(--green)"/>
    </svg>
    <div class="person">
      <p class="person__name">Morris Quimby</p>
      <p class="person__role">Co-Owner</p>
    </div>
    <p class="brand">Quimby's Yard &amp; Garden Center</p>
    <p class="address">4820 County Road M<br>Elmsford, OHIO 43999</p>
    <ul class="contact">
      <li>(555) 201-7784
        <svg viewBox="0 0 24 24"><path d="M5 3h4l2 5-3 2a11 11 0 0 0 6 6l2-3 5 2v4a2 2 0 0 1-2 2A17 17 0 0 1 3 5a2 2 0 0 1 2-2z"/></svg></li>
      <li>(555) 318-6092
        <svg viewBox="0 0 24 24"><rect x="6" y="2" width="12" height="20" rx="2"/><line x1="11" y1="18" x2="13" y2="18"/></svg></li>
      <li>Morris@Quimbysyardandgarden.example
        <svg viewBox="0 0 24 24"><rect x="2" y="5" width="20" height="14"/><path d="M2 5l10 8 10-8"/></svg></li>
      <li>www.Quimbysyardandgarden.example
        <svg viewBox="0 0 24 24"><circle cx="12" cy="12" r="10"/><ellipse cx="12" cy="12" rx="4" ry="10"/><line x1="2" y1="12" x2="22" y2="12"/></svg></li>
    </ul>
  </section>
</main>
</body>
</html>
```